Re-design existing website and add products for sale.

Our current website is very basic and cluttered. (emberfernwellness.com.au)We want a modern looking website that is easy to navigate. We also want to start selling essential oils and crystal products, so there needs to be a separate page for this. Also needs to be easily edited as we need to change the monthly oracle card with the description. Would like calming colours as we are all about natural healing. Alongside the services listed there should be a button to book now which asks for their name, email, phone number ect. and adds it to the cart.

• Logo is still being designed, please leave a space for the logo which will basically be a lotus flower within a mandala.

```html
<!DOCTYPE html>
<html lang="en">
<head>
<meta charset="utf-8">
<title>Ember Fern Wellness</title>
<link href="https://fonts.googleapis.com/css2?family=Lato:wght@400;700;900&display=swap" rel="stylesheet">
<style>
:root{
  --nav:#4b4fc8;
  --magenta:#9a0d6e;
  --blue:#3a41b6;
  --text:#444;
  --muted:#666;
  --grey-band:#eff0f3;
  --dark:#161616;
  --white:#fff;
}
*{box-sizing:border-box;margin:0;padding:0}
html,body{width:1200px;height:2353px;overflow:hidden;background:#fff}
body{font-family:'Lato',sans-serif;color:var(--text)}
.page{position:relative;width:1200px;height:2353px;overflow:hidden}
.abs{position:absolute}

/* header */
.hero{position:absolute;left:0;top:0;width:1200px;height:460px}
.social{position:absolute;left:248px;top:10px;display:flex;gap:8px}
.social a{font-size:11px;color:var(--magenta);text-decoration:none;font-weight:700}
.call{position:absolute;left:874px;top:6px;color:#fff;font-size:11px;font-weight:700;line-height:1.2}
.call strong{display:block;font-size:15px;font-weight:400}
.navbar{position:absolute;left:0;top:39px;width:1200px;height:27px;background:var(--nav)}
.navbar a{position:absolute;top:6px;color:#fff;font-size:12px;text-decoration:none}
.logo-tab{position:absolute;left:537px;top:0;width:126px;height:112px;background:#fff;border-radius:0 0 63px 63px;box-shadow:0 2px 6px rgba(0,0,0,.15);display:flex;flex-direction:column;align-items:center;justify-content:center;gap:6px}
.logo-tab .dot{width:30px;height:30px;border-radius:50%;background:var(--magenta)}
.logo-tab span{color:var(--nav);font-weight:700;font-size:13px;text-align:center;line-height:1.15}
.headline{position:absolute;left:250px;top:216px}
.headline h1{font-size:25px;font-weight:700;color:#fff;line-height:1}
.headline h1 span{display:inline-block;background:var(--nav);padding:5px 6px;margin-bottom:5px}
.headline p{font-size:11.5px;color:#333;width:300px;line-height:1.4;margin-top:6px}
.product-shot{position:absolute;left:800px;top:148px;width:145px;height:230px;border-radius:6px;background:linear-gradient(180deg,#1b2a6a,#3f5fd0 45%,#dfe6ff)}

/* features */
.feature{position:absolute;top:446px;width:163px;height:154px;background:#fff;border:1px solid #ddd;border-radius:10px;box-shadow:0 2px 6px rgba(0,0,0,.08);text-align:center;padding-top:20px}
.feature svg{display:block;margin:0 auto 6px}
.feature h3{font-size:13px;font-weight:700;color:#222;margin-bottom:4px}
.feature p{font-size:8.5px;line-height:1.35;color:var(--muted)}

.services-bg{position:absolute;left:0;top:430px;width:1200px;height:545px;background:linear-gradient(180deg,#fdf8fb,#f6e4ee 60%,#fbf2f6)}
.problem{position:absolute;left:0;top:624px;width:1200px;text-align:center}
.problem h2{color:var(--magenta);font-size:19px;font-weight:700}
.problem p{font-size:8.5px;color:#333;margin-top:2px}
.services{position:absolute;left:250px;top:702px;width:330px}
.services h4{color:var(--magenta);font-size:12px;font-weight:700}
.services .lead{font-size:10px;font-weight:700;color:#222;line-height:1.3;margin-top:2px}
.services ul{list-style:none;margin-top:12px}
.services li{font-size:9px;color:#555;height:18.6px;position:relative;padding-left:13px}
.services li::before{content:"";position:absolute;left:0;top:3px;width:4px;height:4px;border-radius:50%;background:var(--magenta)}
.video{position:absolute;left:578px;top:704px;width:373px;height:222px;border:1px solid var(--magenta);background:linear-gradient(135deg,#c9b89e,#8a6f4f 55%,#2d2823)}
.video .bar{position:absolute;left:0;bottom:0;width:100%;height:34px;background:rgba(0,0,0,.55);display:flex;align-items:center;padding-left:10px;gap:8px;color:#fff;font-size:10px}

/* how */
.how{position:absolute;left:0;top:1022px;width:1200px;text-align:center;color:var(--magenta);font-size:21px;font-weight:700}
.timeline{position:absolute;left:0;top:1075px}
.step-title{position:absolute;width:170px;text-align:center;top:1183px;color:var(--magenta);font-size:12px;font-weight:700}
.step-desc{position:absolute;width:170px;text-align:center;top:1200px;font-size:8.5px;line-height:1.45;color:#555}

/* limitless */
.limitless{position:absolute;left:0;top:1291px;width:601px;height:283px;background:var(--grey-band)}
.limitless-photo{position:absolute;left:601px;top:1291px;width:599px;height:283px;background:linear-gradient(120deg,#e8557c,#d8a36a 45%,#8ca548 80%,#5f7d2c)}
.limitless h2{position:absolute;left:249px;top:30px;color:var(--blue);font-size:20px;font-weight:700}
.limitless .copy{position:absolute;left:249px;top:70px;width:325px}
.limitless .copy p{font-size:8.3px;line-height:1.45;color:#555;margin-bottom:8px}
.btn{display:inline-block;background:var(--magenta);color:#fff;font-size:9.5px;padding:5px 12px;border-radius:12px;text-decoration:none}
.limitless .btn{position:absolute;left:249px;top:234px}

/* about */
.about-photo{position:absolute;border-radius:50%;border:6px solid #9aa0ea;box-shadow:0 0 0 4px #6368d4}
.about{position:absolute;left:563px;top:1621px;width:390px}
.about h2{color:var(--blue);font-size:18px;font-weight:700;margin-bottom:8px}
.about p{font-size:8.3px;line-height:1.5;color:#555;margin-bottom:8px}
.about .btn{margin-top:24px}

/* testimonials */
.testi-bg{position:absolute;left:0;top:1868px;width:1200px;height:305px;background:linear-gradient(180deg,#fff,#f2f1f4)}
.testi-title{position:absolute;left:0;top:1878px;width:1200px;text-align:center;color:var(--blue);font-size:20px;font-weight:700}
.card{position:absolute;top:1923px;width:212px;height:195px;background:#fff;border:1px solid #ddd;text-align:center;padding-top:12px}
.card .avatar{width:70px;height:70px;border-radius:50%;border:2px solid var(--magenta);margin:0 auto;background:linear-gradient(135deg,#f1c9a4,#b9825f)}
.card h4{color:var(--blue);font-size:12px;font-weight:700;margin:10px 0 4px}
.card p{font-size:8.5px;line-height:1.5;color:#777;padding:0 14px}

/* footer */
.footer{position:absolute;left:0;top:2173px;width:1200px;height:180px;background:var(--dark);color:#fff}
.f-logo{position:absolute;left:251px;top:16px;display:flex;flex-direction:column;align-items:center;gap:4px;width:60px}
.f-logo .dot{width:28px;height:28px;border-radius:50%;background:var(--magenta)}
.f-logo span{font-size:9px;font-weight:700;text-align:center;line-height:1.1}
.f-about{position:absolute;left:318px;top:20px;width:240px;font-size:8px;line-height:1.4}
.f-contact{position:absolute;left:658px;top:24px;font-size:10.5px}
.f-contact p{margin-bottom:10px}
.f-social{position:absolute;left:904px;top:24px;font-size:10.5px}
.f-social small{display:block;font-size:8px;margin-top:10px}
.f-rule{position:absolute;left:0;width:1200px;height:1px;background:#2c2c2c}
.f-nav{position:absolute;left:0;top:102px;width:1200px;text-align:center;font-size:10.5px}
.f-nav a{color:#fff;text-decoration:none;margin:0 10px}
.f-nav a.active{color:var(--magenta)}
.f-copy{position:absolute;left:0;top:163px;width:1200px;text-align:center;font-size:7px}
</style>
</head>
<body>
<div class="page">

  <!-- hero -->
  <svg class="hero" viewBox="0 0 1200 460" aria-hidden="true">
    <defs>
      <linearGradient id="heroFill" x1="0" y1="0" x2="1" y2="1">
        <stop offset="0" stop-color="#bfe6dc"/>
        <stop offset=".45" stop-color="#d6f0ea"/>
        <stop offset=".75" stop-color="#a8dcd4"/>
        <stop offset="1" stop-color="#c7e7b0"/>
      </linearGradient>
    </defs>
    <path d="M0 0H1200V430Q600 330 0 430Z" fill="url(#heroFill)"/>
  </svg>
  <div class="abs" role="img" aria-label="Soft light over people meditating" style="left:0;top:0;width:1200px;height:430px;background:radial-gradient(circle at 700px 180px,rgba(255,255,255,.7),rgba(255,255,255,0) 320px)"></div>

  <nav class="social"><a href="#">Facebook</a><a href="#">Instagram</a></nav>
  <div class="call">Call Us<strong>0400 318 972</strong></div>
  <div class="navbar">
    <a href="#" style="left:380px">Home</a>
    <a href="#" style="left:431px">About</a>
    <a href="#" style="left:482px">Product</a>
    <a href="#" style="left:681px">Book</a>
    <a href="#" style="left:728px">Courses</a>
    <a href="#" style="left:788px">Contact</a>
  </div>
  <div class="logo-tab"><div class="dot"></div><span>Ember Fern<br>Wellness</span></div>

  <div class="headline">
    <h1><span>Find Your True Self and</span><br><span>Bring Balance to Your Life</span></h1>
    <p>Overcome anxiety and mental noise with the power of meditation, wisdom and awareness.</p>
  </div>
  <div class="product-shot" role="img" aria-label="Three roll-on essential oil bottles"></div>

  <!-- services band -->
  <div class="services-bg" role="img" aria-label="Faded photo of a meditation class"></div>

  <div class="feature" style="left:323px">
    <svg width="36" height="36" viewBox="0 0 36 36" fill="none" stroke="#9a0d6e" stroke-width="1.6"><circle cx="18" cy="14" r="5"/><path d="M18 3v3M8 8l2 2M28 8l-2 2M4 16h3M29 16h3M10 33h16M18 19v10M12 26l6-4 6 4"/></svg>
    <h3>CALM</h3>
    <p>Have peace of mind<br>be present and undisturbed.<br>Live with confidence and clarity</p>
  </div>
  <div class="feature" style="left:519px">
    <svg width="36" height="36" viewBox="0 0 36 36" fill="none" stroke="#9a0d6e" stroke-width="1.6"><path d="M7 20v-4a11 11 0 0 1 22 0v4"/><rect x="5" y="19" width="6" height="9" rx="2"/><rect x="25" y="19" width="6" height="9" rx="2"/><path d="M28 28q0 5-8 5"/></svg>
    <h3>CENTERED</h3>
    <p>Remember who you are.<br>Don't be bullied by your thoughts.<br>Find emotional balance and stability.</p>
  </div>
  <div class="feature" style="left:715px">
    <svg width="36" height="36" viewBox="0 0 36 36" fill="none" stroke="#9a0d6e" stroke-width="1.6"><path d="M18 32S4 23 4 13a7 7 0 0 1 14-2 7 7 0 0 1 14 2c0 10-14 19-14 19z"/><circle cx="18" cy="17" r="4"/><path d="M18 10v3M18 21v3M11 17h3M22 17h3"/></svg>
    <h3>FOCUSED</h3>
    <p>Master the scattered mind.<br>Achieve your goals.<br>live a life purpose.</p>
  </div>

  <div class="problem">
    <h2>Sounds good.. but life is often different...</h2>
    <p>What prevents you from living a life like that is clam, centered and focused?</p>
  </div>

  <div class="services">
    <h4>Some of the services on offer include</h4>
    <p class="lead">how do you know if you have a mind like that?<br>see if you experience any of the challenges that often come with it:</p>
    <ul>
      <li>Reiki &amp; Seichim Healings</li>
      <li>Energy Healing</li>
      <li>Chakra Balancing</li>
      <li>Energy Balancing</li>
      <li>Past Life Clearing</li>
      <li>Oracle Card Readings/Online Readings</li>
      <li>Distant Healing</li>
      <li>Reiki &amp; Seichim Workshops</li>
      <li>Crystals &amp; Hand Made Jewellery Available</li>
      <li>Essential Oil Roll On Blends Available</li>
    </ul>
  </div>
  <div class="video" role="img" aria-label="Video still of singing bowls on a table">
    <div class="bar">
      <svg width="20" height="20" viewBox="0 0 20 20"><circle cx="10" cy="10" r="9" fill="none" stroke="#c0168a" stroke-width="1.5"/><path d="M8 6l6 4-6 4z" fill="#c0168a"/></svg>
      Master your mind, master your life!
    </div>
  </div>

  <!-- how it works -->
  <h2 class="how">How Does it work?</h2>
  <svg class="timeline" width="1200" height="110" viewBox="0 1075 1200 110" fill="none">
    <g stroke="#555" stroke-width="1.3">
      <path d="M347 1100c-6-8-6-15 0-22 6 7 6 14 0 22zM347 1100c-10 0-16-6-17-13 8 0 14 5 17 13zM347 1100c10 0 16-6 17-13-8 0-14 5-17 13zM333 1102h28"/>
      <circle cx="516" cy="1085" r="4"/><path d="M516 1089v10M506 1094l10-3 10 3M503 1108l13-8 13 8z"/>
      <circle cx="690" cy="1087" r="3.5"/><path d="M690 1091l-6 14M684 1105l-10 0M684 1105h12M684 1098l12-4"/><path d="M670 1110h28"/>
      <circle cx="852" cy="1083" r="4"/><path d="M852 1087v14M843 1080l9 10 9-10M846 1112l6-11 6 11"/>
    </g>
    <line x1="254" y1="1153" x2="946" y2="1153" stroke="#9a0d6e" stroke-width="2"/>
    <circle cx="254" cy="1153" r="4" fill="#fff" stroke="#9a0d6e" stroke-width="2"/>
    <circle cx="946" cy="1153" r="4" fill="#9a0d6e"/>
    <g font-family="Lato,sans-serif" font-size="9" font-weight="700" fill="#fff" text-anchor="middle">
      <circle cx="347" cy="1153" r="24" fill="#b6b9ee"/><circle cx="347" cy="1153" r="18" fill="#4b4fc8"/><text x="347" y="1151">1</text><text x="347" y="1161">Step</text>
      <circle cx="516" cy="1153" r="24" fill="#b6b9ee"/><circle cx="516" cy="1153" r="18" fill="#4b4fc8"/><text x="516" y="1151">2</text><text x="516" y="1161">Step</text>
      <circle cx="684" cy="1153" r="24" fill="#b6b9ee"/><circle cx="684" cy="1153" r="18" fill="#4b4fc8"/><text x="684" y="1151">3</text><text x="684" y="1161">Step</text>
      <circle cx="852" cy="1153" r="24" fill="#b6b9ee"/><circle cx="852" cy="1153" r="18" fill="#4b4fc8"/><text x="852" y="1151">4</text><text x="852" y="1161">Step</text>
    </g>
  </svg>
  <div class="step-title" style="left:262px">Meditation</div>
  <div class="step-desc" style="left:262px">Find your ideal meditation<br>build a daily practice integrate<br>it in your life.</div>
  <div class="step-title" style="left:431px">Inner Work</div>
  <div class="step-desc" style="left:431px">Master the inner voice<br>upgrade your mindsets let go<br>of negative narratives</div>
  <div class="step-title" style="left:599px">Conscious Living</div>
  <div class="step-desc" style="left:599px">Live with wisdom &amp; courage<br>cultivate mindfulness expand<br>your limits</div>
  <div class="step-title" style="left:767px">Transcendenc</div>
  <div class="step-desc" style="left:767px">Find your ideal meditation<br>build a daily practice integrate<br>it in your life.</div>

  <!-- limitless life -->
  <section class="limitless">
    <h2>Limitless Life</h2>
    <div class="copy">
      <p>Limitless life is Brightpath's unique membership program, covering all of four elements. it includes a suite of online courses, guided meditations, teacher interactions, and a supportive community of conscious individuals.</p>
      <p>Limitless life exists to give you ongoing support and structure to increase emotional wellbeing and presonal growth in your life. Each day you will receive a short lesson that is simple actionable and effective. Think of it as the gym membership for your mind, heart and soul.</p>
      <p>eal self-transformation requires more than some headspace. Medition is just first step. Drawing form the wisdom of contemplative tradition of the East,Positive psychology and personal development literature, Limitless life has all the tools you need to live a life that is calm, centered and focused.</p>
    </div>
    <a class="btn" href="#">Join The Limitless Life program</a>
  </section>
  <div class="limitless-photo" role="img" aria-label="Person meditating on grass beside a singing bowl"></div>

  <!-- about -->
  <div class="about-photo" role="img" aria-label="Portrait of the healer with family" style="left:251px;top:1624px;width:204px;height:204px;background:linear-gradient(135deg,#d8cbd9,#8a6d86 60%,#4c3e62)"></div>
  <div class="about-photo" role="img" aria-label="Portrait of the healer in a red head wrap" style="left:397px;top:1702px;width:142px;height:142px;background:linear-gradient(135deg,#4a8fa8,#c2504e 55%,#e3b49c)"></div>
  <section class="about">
    <h2>About Clara Veshmore</h2>
    <p>My love of all things spiritual and holistic started as a young girl and deepened when I first studied Reiki 19 years ago in 2000.</p>
    <p>After suffering with a hereditary medical problem from early childhood, I set about finding a solution in conjunction with modern medicine, which would enable me to get through each day both calmer and stronger, while feeling more vibrant and alive.</p>
    <p>It was not until 2016 however, that I finally realised I wanted to use my training and abilities to help the wider community, rather than just those close to me. With that in mind, I set about gaining my Reiki Master/Teacher and Seichim Master/Teacher qualifications to not only help those requiring</p>
    <a class="btn" href="#">Read More</a>
  </section>

  <!-- testimonials -->
  <div class="testi-bg"></div>
  <h2 class="testi-title">Testimonial</h2>
  <div class="card" style="left:249px"><div class="avatar" role="img" aria-label="Client portrait"></div><h4>Milo Hartwell</h4><p>Contrary to popular belief, Lorem Ipsum is not simply random text. It has roots in a piece of classical Latin literature from 45 BC, making it over 2000 years old. Peter Ashdown.</p></div>
  <div class="card" style="left:494px"><div class="avatar" role="img" aria-label="Client portrait"></div><h4>Milo Hartwell</h4><p>Contrary to popular belief, Lorem Ipsum is not simply random text. It has roots in a piece of classical Latin literature from 45 BC, making it over 2000 years old. Peter Ashdown.</p></div>
  <div class="card" style="left:739px"><div class="avatar" role="img" aria-label="Client portrait"></div><h4>Milo Hartwell</h4><p>Contrary to popular belief, Lorem Ipsum is not simply random text. It has roots in a piece of classical Latin literature from 45 BC, making it over 2000 years old. Peter Ashdown.</p></div>

  <!-- footer -->
  <footer class="footer">
    <div class="f-logo"><div class="dot"></div><span>Ember Fern Wellness</span></div>
    <p class="f-about">Lorem Ipsum is simply dummy text of the printing and typesetting industry. Lorem Ipsum has been the industry's standard dummy text ever Lorem Ipsum is simply dummy text of the printing and typesetting industry.</p>
    <div class="f-contact"><p>Contact us for details</p><p>Email Us: info@emberfernwellness.com.au</p></div>
    <div class="f-social">Get Social<small>Facebook &nbsp; Twitter</small></div>
    <div class="f-rule" style="top:84px"></div>
    <nav class="f-nav"><a class="active" href="#">Home</a><a href="#">About</a><a href="#">Blog</a><a href="#">Podcast</a><a href="#">Book</a><a href="#">Courses</a><a href="#">Coaching</a></nav>
    <div class="f-rule" style="top:148px"></div>
    <p class="f-copy">© Copyright 2019 | All Rights Reserved</p>
  </footer>
</div>
</body>
</html>
```